Design a double sided business card

We are looking for a clean, eye-catching, and contemporary design that enhances the brand and presents a premium, professional image. Our preference is for a brown card with black gloss detailing and embossed elements; however, we are open to creative input and design suggestions that best achieve a strong visual impact.

Please see the attached existing business card for reference. We use both black and brown colours consistently across our branding.

On sample provided

```html
<!DOCTYPE html>
<html lang="en">
<head>
<meta charset="utf-8">
<title>Steinwerk business card</title>
<link href="https://fonts.googleapis.com/css2?family=Montserrat:wght@400;500;700;800&display=swap" rel="stylesheet">
<style>
  :root {
    --ink: #161616;
    --tan: #c9b49a;
    --paper: #ffffff;
    --stage: #3a3a3a;
  }
  html, body { margin: 0; padding: 0; overflow: hidden; }
  body {
    width: 1200px; height: 1200px;
    background: var(--stage);
    font-family: "Montserrat", sans-serif;
    position: relative;
  }
  .card {
    position: absolute;
    left: 160px;
    width: 880px; height: 540px;
    border-radius: 40px;
    overflow: hidden;
  }
  .card--front { top: 50px; background: var(--paper); }
  .card--back { top: 620px; background: var(--ink); }
  .card__bands { position: absolute; inset: 0; }

  .brand { position: absolute; display: flex; align-items: center; }
  .brand__square { border: 7px solid currentColor; box-sizing: border-box; }
  .brand__name { font-weight: 800; letter-spacing: 0.12em; }

  .card--front .brand { left: 200px; top: 80px; color: var(--ink); }
  .card--front .brand__square { width: 84px; height: 84px; }
  .brand__divider { width: 3px; height: 96px; background: var(--ink); margin: 0 24px; }
  .card--front .brand__name { font-size: 52px; }

  .rule { position: absolute; height: 1.5px; background: var(--tan); }
  .rule--top { left: 190px; top: 215px; width: 620px; }
  .rule--name { left: 60px; top: 380px; width: 380px; }

  .person { position: absolute; left: 60px; top: 282px; }
  .person__name { font-size: 40px; font-weight: 700; color: var(--tan); line-height: 1; }
  .person__role { font-size: 26px; font-weight: 500; color: var(--ink); margin-top: 6px; letter-spacing: 0.02em; }

  .contact { position: absolute; list-style: none; margin: 0; padding: 0; color: var(--ink); }
  .contact li { display: flex; align-items: flex-start; gap: 14px; }
  .contact svg { flex: none; width: 26px; height: 26px; fill: var(--tan); margin-top: 3px; }
  .contact--phones { left: 60px; top: 395px; font-size: 30px; font-weight: 500; }
  .contact--phones li { margin-bottom: 8px; }
  .contact--details { left: 530px; top: 240px; font-size: 23px; line-height: 1.3; }
  .contact--details li { margin-bottom: 8px; }

  .website { position: absolute; right: 60px; top: 450px; color: var(--paper); font-size: 24px; letter-spacing: 0.04em; }

  .card--back .brand { left: 0; right: 0; top: 0; bottom: 0; flex-direction: column; justify-content: center; color: var(--tan); }
  .card--back .brand__square { width: 150px; height: 150px; border-width: 10px; margin-bottom: 34px; }
  .card--back .brand__name { font-size: 74px; }
</style>
</head>
<body>

<section class="card card--front" aria-label="Card front">
  <svg class="card__bands" viewBox="0 0 880 540" aria-hidden="true">
    <path d="M0 478 L470 478 C540 478 540 392 610 392 L880 392 L880 540 L0 540 Z" fill="var(--tan)"/>
    <path d="M0 500 L490 500 C560 500 560 414 630 414 L880 414 L880 540 L0 540 Z" fill="var(--ink)"/>
  </svg>

  <div class="brand">
    <span class="brand__square"></span>
    <span class="brand__divider"></span>
    <span class="brand__name">STEINWERK</span>
  </div>

  <div class="rule rule--top"></div>

  <div class="person">
    <div class="person__name">RAVI DHILLON</div>
    <div class="person__role">DIRECTOR</div>
  </div>
  <div class="rule rule--name"></div>

  <ul class="contact contact--phones">
    <li>
      <svg viewBox="0 0 24 24"><path d="M6.6 10.8a15.1 15.1 0 0 0 6.6 6.6l2.2-2.2a1 1 0 0 1 1-.25 11.4 11.4 0 0 0 3.6.57 1 1 0 0 1 1 1V20a1 1 0 0 1-1 1A17 17 0 0 1 3 4a1 1 0 0 1 1-1h3.5a1 1 0 0 1 1 1c0 1.25.2 2.45.57 3.57a1 1 0 0 1-.25 1z"/></svg>
      <span>0800 214 7730</span>
    </li>
    <li>
      <svg viewBox="0 0 24 24"><path d="M7 1h10a2 2 0 0 1 2 2v18a2 2 0 0 1-2 2H7a2 2 0 0 1-2-2V3a2 2 0 0 1 2-2zm0 3v15h10V4zm5 16.2a1 1 0 1 0 0 1.6 1 1 0 0 0 0-1.6z"/></svg>
      <span>07700900461</span>
    </li>
  </ul>

  <ul class="contact contact--details">
    <li>
      <svg viewBox="0 0 24 24"><path d="M2 5h20v14H2zm2 2v.4l8 5.2 8-5.2V7zm0 2.8V17h16V9.8l-8 5.2z"/></svg>
      <span>ravi@steinwerk.co.uk</span>
    </li>
    <li>
      <svg viewBox="0 0 24 24"><path d="M12 2a7 7 0 0 1 7 7c0 5-7 13-7 13S5 14 5 9a7 7 0 0 1 7-7zm0 4.5a2.5 2.5 0 1 0 0 5 2.5 2.5 0 0 0 0-5z"/></svg>
      <span>12 Millbrook Lane<br>Eastfield AB1 2CD</span>
    </li>
  </ul>

  <div class="website">www.steinwerk.co.uk</div>
</section>

<section class="card card--back" aria-label="Card back">
  <div class="brand">
    <span class="brand__square"></span>
    <span class="brand__name">STEINWERK</span>
  </div>
</section>

</body>
</html>
```